Coaching company requires a Bi-Fold Services Brochure

**Please also read attached design brief***

As part of our expanding sales role for our Professional Development Company, we need a Bi-Fold services brochure that offers our clients some further information about our specific services.

This services brochure will be the document that our clients will receive after our initial contact with them so the overall design of this document will play an instrumental part in our securing of ongoing work.

We have prepared a design brief for designers that want to undertake this task and this document should help to clarify any missing information from this online brief. Any designer who is interested in submitting a design should also refer to this attached document to get the full scope of the works required.

Regular email correspondence will also be available to clarify any questions that the design may have

*** Please also note that the finished design will need to be submitted in a PSD format to allow for editing in Photoshop CS6

Target Market(s)

Our target market is Business to Business. We are specifically targeting small, medium and large businesses who are looking to invest in Professional Development for their business and their staff.
The areas of major focus are 1 on 1 coaching of leaders, executives & business owners and group facilitation sessions with their staff.

Industry/Entity Type

Business Service

Font styles to use
Sans Serif

Requirements
Must have
• - Design needs to be an A4 Bi-Fold layout so should suit an A3 sheet of paper (297mm x 420mm)
• - Include our corporate color scheme
• - Finished design must be in PSD format or format that can be edited in Photshop CS6
• - Appealing to small, medium and large businesses (universal appeal)
• - The project must be in CMYK Colour and no less than 300 pixel resolution
Nice to have
• - Our logo incorporated into the front page
• - We would like the images used in this brochure to be happy and vibrant (i.e. smiling faces and energetic etc.)

```html
<!DOCTYPE html>
<html lang="en">
<head>
<meta charset="utf-8">
<title>Vantage PD – Services Brochure</title>
<link href="https://fonts.googleapis.com/css2?family=Open+Sans:ital,wght@0,300;0,400;0,600;0,700;1,300;1,400&family=Raleway:wght@300;400&family=Oswald:wght@400&display=swap" rel="stylesheet">
<style>
  :root{
    --blue:#2f5bb0;
    --blue-deep:#1d3f8f;
    --grey-dark:#5c5c5c;
    --grey-mid:#8d8d8d;
    --paper:#ffffff;
    --ink:#2a2a2a;
    --backdrop:#8f8f8f;
  }
  *{box-sizing:border-box;margin:0;padding:0}
  html,body{width:1200px;height:1032px;overflow:hidden}
  body{background:radial-gradient(ellipse at 50% 45%,#a8a8a8,var(--backdrop) 70%);font-family:'Open Sans',sans-serif;color:var(--ink)}
  .spread{position:absolute;left:40px;top:120px;width:1120px;height:792px;display:flex;box-shadow:0 14px 40px rgba(0,0,0,.35)}
  .page{position:relative;width:560px;height:792px;background:var(--paper);overflow:hidden}
  .page--left{background:linear-gradient(90deg,#fff 80%,#eceef2)}
  .page--right{background:linear-gradient(90deg,#e9ebef,#fff 18%)}
  .abs{position:absolute}
  svg.shape{position:absolute;left:0;top:0}
  .dropcap::first-letter{float:left;font-size:28px;line-height:.9;color:var(--blue);margin-right:3px}

  /* left page */
  .site-url{right:34px;top:14px;color:#fff;font-size:11px;letter-spacing:5px;font-weight:300}
  .join-title{right:30px;top:30px;color:#fff;font-family:'Raleway',sans-serif;font-weight:300;font-size:40px;letter-spacing:1px}
  .about-label{right:36px;top:100px;font-family:'Raleway',sans-serif;font-size:20px;letter-spacing:14px;color:var(--grey-dark)}
  .brand{left:48px;top:150px;display:flex;align-items:center;gap:6px;font-size:15px;font-weight:600;color:var(--blue-deep)}
  .brand .dot{width:12px;height:12px;border-radius:50%;background:var(--blue-deep)}
  .intro{left:200px;top:156px;width:330px;font-size:10px;line-height:1.45}
  .intro p{margin-bottom:7px}
  .intro p.wide{margin-left:-160px;width:490px}
  .photo{position:absolute}
  .photo--team{left:0;top:430px;width:560px;height:150px;background:linear-gradient(90deg,#6f88b8,#3c3f82 30%,#7a6aa8 55%,#b5c9e0 80%,#e8eef6)}
  .results{left:70px;top:592px;display:flex;align-items:flex-end;gap:6px}
  .results .lead{font-size:17px;line-height:1.05}
  .results .big{font-size:44px;line-height:.9;letter-spacing:1px}
  .results-copy{left:140px;top:646px;width:400px;font-size:11px;line-height:1.38}

  /* right page */
  .services-title{right:28px;top:10px;color:#fff;font-family:'Raleway',sans-serif;font-weight:300;font-size:44px}
  .tab{position:absolute;height:26px;padding:0 14px;display:flex;align-items:center;color:#fff;font-family:'Oswald',sans-serif;font-size:16px;letter-spacing:.5px;background:var(--blue);clip-path:polygon(0 0,100% 0,94% 100%,0 100%);border-left:4px solid var(--blue-deep)}
  .tab--coaching{left:22px;top:84px;width:200px}
  .tab--group{left:34px;top:522px;width:230px}
  .tab--courses{left:296px;top:512px;width:240px}
  .photo--class{left:290px;top:78px;width:250px;height:150px;background:linear-gradient(110deg,#2b2b2b,#454545 55%,#8a8f9a 75%,#cfd3da)}
  .photo--meeting{left:22px;top:356px;width:518px;height:148px;background:linear-gradient(100deg,#c9c2b8,#e4e2de 35%,#8d6a64 60%,#5e6676 85%,#b9bcc2)}
  .svc{font-size:8.5px;line-height:1.35}
  .svc h4{font-weight:300;font-style:italic;font-size:9px;color:var(--grey-mid);margin-bottom:1px}
  .svc h4::before{content:"";display:inline-block;border-left:6px solid var(--blue);border-top:4px solid transparent;border-bottom:4px solid transparent;margin-right:6px}
  .svc--coaching{left:30px;top:116px;width:250px}
  .svc--exec{left:30px;top:250px;width:510px}
  .svc--small{left:30px;top:300px;width:510px}
  .col{font-size:9px;line-height:1.42}
  .col p{margin-bottom:6px}
  .col--group{left:40px;top:558px;width:230px}
  .col--courses{left:300px;top:548px;width:238px}
  .people-figures{left:440px;top:682px;width:100px;height:72px;background:linear-gradient(90deg,#7d7d7d,#c45a2a 45%,#8a8a8a 60%,#bdbdbd)}
</style>
</head>
<body>
<main class="spread">

  <section class="page page--left">
    <svg class="shape" width="560" height="792" aria-hidden="true">
      <polygon points="0,0 560,0 560,96 380,96 300,140 0,140" fill="var(--blue)"/>
      <polygon points="0,0 560,0 560,20 0,60" fill="var(--blue-deep)" opacity=".45"/>
      <polygon points="110,60 200,150 110,240 20,150" fill="#cfd0d4"/>
      <polygon points="110,66 194,150 110,234 26,150" fill="#e3e4e7"/>
      <polygon points="0,758 220,746 560,762 560,792 0,792" fill="var(--blue)"/>
      <polygon points="0,770 140,792 0,792" fill="var(--blue-deep)"/>
    </svg>
    <div class="abs site-url">www.vantagepd.com.au</div>
    <h1 class="abs join-title">JOIN OUR TEAM</h1>
    <div class="abs about-label">ABOUT US</div>
    <div class="abs brand"><span class="dot"></span>Vantage PD</div>

    <div class="abs intro">
      <p class="dropcap">Vantage PD is a professional development company, who specialises in assisting all levels of business with the development of their most valued asset... their people!</p>
      <p>Working closely with our clients, we assist them to build and adopt highly successful "people centric" cultures and philosophies that resonate throughout their entire business.</p>
      <p class="wide">From front line operators all the way to the treatment of your clients, we help your business to ingrain an everlasting "human focused" principals that increase personal performance, drive innovation and change, increase customer satisfaction levels, ensure repeat business and builds a reputation for your business that outshines your competitors!</p>
    </div>

    <div class="photo photo--team" role="img" aria-label="Photo of a business team in silhouette meeting around a table against a city skyline"></div>

    <div class="abs results"><span class="lead">How we<br>deliver</span><span class="big">RESULTS</span></div>
    <p class="abs results-copy dropcap">From tailored Leadership development coaching to the design and delivery of operational strategies, we are with you every step of the way! After establishing your businesses unique requirements, we utilise a multiple of different professional development services to help you establish a strong "people centric" culture and philosophy across your entire business structure.</p>
  </section>

  <section class="page page--right">
    <svg class="shape" width="560" height="792" aria-hidden="true">
      <defs>
        <linearGradient id="band" x1="0" x2="1">
          <stop offset="0" stop-color="#4a4a4a"/><stop offset="1" stop-color="#9a9a9a"/>
        </linearGradient>
      </defs>
      <polygon points="0,0 560,0 560,62 40,70 0,80" fill="url(#band)"/>
      <polygon points="0,764 120,776 150,792 0,792" fill="var(--blue)"/>
    </svg>
    <h2 class="abs services-title">OUR SERVICES</h2>

    <div class="tab tab--coaching">COACHING</div>
    <div class="photo photo--class" role="img" aria-label="Photo of a smiling coach writing Learn and Lead on a chalkboard"></div>
    <div class="abs svc svc--coaching">
      <h4>"People Centric" Leadership Coaching:</h4>
      <p>Our "People Centric" Leadership Coaching Service is specifically designed to assist new, existing and emerging leaders to identify and harness their true leadership potential to create a resonating people based culture throughout their business. This also includes obtaining their immediate and long term leadership goals, as well as their most important personal development needs, all within the shortest time possible.</p>
    </div>
    <div class="abs svc svc--exec">
      <h4>Executive Coaching:</h4>
      <p>Our Executive Coaching sessions provide experienced business owners, managing directors and senior executives with personalised, one on one, self-propelled development that aligns thoughts, feelings and actions to gain instant clarity and traction and produce results.</p>
    </div>
    <div class="abs svc svc--small">
      <h4>Small Business Coaching:</h4>
      <p>Our Small Business Coaching provides business owners and managers with self- directed strategic and business development tools and actions designed to drive their business forward. From the creation of a Vision, all the way through to strategic develop plans, we can help you paint that clear picture and follow through to achieve your desired outcomes.</p>
    </div>

    <div class="photo photo--meeting" role="img" aria-label="Photo of a coach in conversation with a young professional in a bright office"></div>

    <div class="tab tab--group">GROUP FACILITATION</div>
    <div class="abs col col--group">
      <p class="dropcap">Our Group Facilitation Service utilises thorough planning, skilful guidance, and expert group management techniques to provide your team with clear "outside the box" thinking, enthusiastic participation and full "buy in" to reach their desired outcomes.</p>
      <p>So if you are looking for expert guidance to find those elusive business solutions, drive your business and operational concepts forward and combine the skills, knowledge and motivation of your teams, then our Group Facilitation Service will suit your needs!</p>
    </div>

    <div class="tab tab--courses">CUSTOMISED COURSES</div>
    <div class="abs col col--courses">
      <p class="dropcap">Unlike the traditional "one boot fits all" approach to training, we work closely with your business to identify skills gap and create courses that will meet your immediate training needs. Through the creation and delivery of tailor-made training content, we can ensure that your business is receiving the right training with the right outcomes and guaranteed to bridge those immediate knowledge gaps.</p>
    </div>

    <div class="abs people-figures" role="img" aria-label="Illustration of a group of grey figures with one orange figure standing out"></div>
  </section>

</main>
</body>
</html>
```